Wordpress Design

Need a responsive wordpress website with the minimum 10 service description pages. This website is for a small business consultancy, providing business development and digital marketing services.

Will also need at least 4 diffrent templates: Home page, service page, Landing Page and blog.

The site will be using block editor.

Coded - Design and coding required

1 page

Sans Serif
• Segoe UI

```html
<!DOCTYPE html>
<html lang="en">
<head>
<meta charset="utf-8">
<title>Clearpath Advisory – Business &amp; Marketing Consultancy</title>
<link rel="stylesheet" href="https://fonts.googleapis.com/css2?family=Open+Sans:wght@400;600;700;800&display=swap">
<style>
:root{
  --blue:#1e9bea;
  --blue-dark:#0f7fc9;
  --ink:#1d2733;
  --text:#4a5563;
  --muted:#7b8592;
  --hero-bg:#f4f6f8;
  --card-border:#e6eaee;
  --funnel-bg:#ececec;
  --cta-band:#5ab6ee;
  --footer:#0b0b0b;
  --white:#fff;
}
*{box-sizing:border-box;margin:0;padding:0}
html,body{width:1200px;height:2556px;overflow:hidden}
body{font-family:"Open Sans",sans-serif;color:var(--text);background:var(--white);position:relative}
.header{position:absolute;top:0;left:0;width:1200px;height:72px;display:flex;align-items:center;padding:0 110px 0 36px;background:var(--white)}
.brand{display:flex;align-items:center;gap:10px;font-weight:700;font-size:22px;color:var(--ink)}
.brand-dot{width:30px;height:30px;border-radius:50%;background:var(--blue)}
.nav{margin-left:auto;display:flex;align-items:center;gap:30px;font-size:14px;font-weight:600;color:var(--ink)}
.nav .active{color:var(--blue)}
.btn{display:inline-block;background:var(--blue);color:var(--white);font-weight:700;font-size:14px;letter-spacing:.5px;text-transform:uppercase;border-radius:4px;padding:11px 22px;white-space:nowrap}
.hero{position:absolute;top:72px;left:0;width:1200px;height:628px;background:var(--hero-bg);overflow:hidden}
.hero-graphics{position:absolute;left:30px;top:16px;width:490px;height:120px;border-radius:10px;background:linear-gradient(90deg,#e4eef6,#eef3e4)}
.hero-photo{position:absolute;left:590px;top:0;width:520px;height:560px;background:linear-gradient(160deg,#dfe4e6,#c9d4d6 55%,#6fa8a6)}
.hero-copy{position:absolute;left:80px;top:150px;width:480px}
.hero-copy h1{font-size:36px;font-weight:800;color:var(--ink);line-height:1.15;margin-bottom:12px;white-space:nowrap}
.hero-copy p{font-size:15px;line-height:1.5;color:var(--text)}
.hero-copy h2{font-size:22px;font-weight:700;color:var(--ink);margin:26px 0 8px}
.signup{display:flex;gap:14px;margin-top:40px}
.signup .field{width:260px;height:46px;background:var(--white);border:1px solid #d7dde3;border-radius:4px;font-size:13px;color:var(--muted);padding:14px}
.signup .btn{height:46px;padding:14px 22px}
.hero-cta{position:absolute;left:700px;top:566px}
.intro{position:absolute;top:790px;left:200px;width:800px;text-align:center;font-size:14px;line-height:1.55}
.intro strong{display:block;margin-top:22px;font-size:18px;color:var(--ink)}
.services{position:absolute;top:955px;left:100px;width:1000px;display:grid;grid-template-columns:repeat(4,235px);gap:20px 20px}
.service{height:180px;border:1px solid var(--card-border);border-radius:6px;box-shadow:0 4px 14px rgba(0,0,0,.06);display:flex;flex-direction:column;align-items:center;padding-top:32px;text-align:center;font-weight:700;font-size:15px;color:var(--ink);line-height:1.35}
.service svg{width:48px;height:48px;margin-bottom:18px;stroke:var(--blue);fill:none;stroke-width:2.5}
.funnel-section{position:absolute;top:1410px;left:0;width:1200px;height:470px;background:var(--funnel-bg)}
.funnel-title{position:absolute;left:180px;top:70px;width:440px;text-align:center;font-size:30px;font-weight:800;color:#3f4a55}
.funnel-art{position:absolute;left:150px;top:130px;width:480px;height:300px;border-radius:6px;background:linear-gradient(180deg,#f1d6cf,#dbe8cf 50%,#cfe6f0 75%,#f4e7bd)}
.funnel-copy{position:absolute;left:715px;top:125px;width:340px}
.funnel-copy h3{font-size:20px;font-weight:700;color:var(--blue-dark);margin-bottom:14px}
.funnel-copy p{font-size:14px;line-height:1.6;margin-bottom:30px}
.dots{display:flex;gap:10px;margin-top:34px}
.dots span{width:14px;height:14px;border-radius:50%;border:2px solid var(--ink)}
.dots span:first-child{background:var(--ink)}
.cta-band{position:absolute;top:1880px;left:0;width:1200px;height:410px;background:var(--cta-band)}
.cta-panel{position:absolute;left:100px;top:60px;width:1000px;height:300px;background:var(--white);border-radius:4px;text-align:center;padding-top:48px}
.cta-panel h2{font-size:28px;font-weight:700;color:var(--ink);line-height:1.3}
.cta-panel p{font-size:24px;color:var(--ink);margin:14px 0 30px;line-height:1.3}
.footer{position:absolute;top:2290px;left:0;width:1200px;height:266px;background:var(--footer);color:var(--white)}
.contacts{position:absolute;top:46px;left:150px;width:900px;display:flex;justify-content:space-between}
.contact{width:220px;text-align:center;font-size:16px;font-weight:600;line-height:1.4}
.contact .circle{width:60px;height:60px;border-radius:50%;background:var(--blue);margin:0 auto 16px;display:flex;align-items:center;justify-content:center}
.contact svg{width:28px;height:28px;fill:none;stroke:var(--white);stroke-width:2.2}
.copyright{position:absolute;bottom:18px;width:100%;text-align:center;font-size:12px;color:#aaa}
</style>
</head>
<body>
<header class="header">
  <div class="brand"><span class="brand-dot"></span>Clearpath Advisory</div>
  <nav class="nav">
    <span class="active">Business Strategy</span><span>Marketing Strategy</span><span>Blog</span><span>About Us</span>
    <span class="btn">Contact us</span>
  </nav>
</header>

<section class="hero">
  <div class="hero-graphics" role="img" aria-label="Illustration of business charts, a pie chart, a light bulb and a calculator"></div>
  <div class="hero-photo" role="img" aria-label="Photo of a smiling businesswoman seated in a teal armchair holding a tablet"></div>
  <div class="hero-copy">
    <h1>That feeling get when...</h1>
    <p>You decide to start your own business and realise you need more than 24 hours to get it all done</p>
    <h2>Introducing Clearpath Advisory</h2>
    <p>We are here to get you started or just share the load of business optimisation and marketing, so you can concentrate on what you are best at!</p>
    <div class="signup"><div class="field">Email address/Phone number</div><span class="btn">Get help now!</span></div>
  </div>
  <span class="btn hero-cta">Let's get you closer to your customers</span>
</section>

<section class="intro">
  <p>At Clearpath Advisory, it's never a one size fits all approach. We are strategy-first consultancy with your customer in mind. Our aim is clearly understanding a clear roadmap, and tackle your highest value projects.</p>
  <strong>All our efforts are concentrated on reaching your customers where they are - getting you closer to you customers</strong>
</section>

<section class="services">
  <div class="service"><svg viewBox="0 0 48 48"><rect x="4" y="8" width="14" height="14"/><rect x="30" y="8" width="14" height="14"/><rect x="4" y="28" width="14" height="14"/><rect x="30" y="28" width="14" height="14"/><path d="M18 15h12M18 35h12"/></svg>Business consultancy<br>and advisory</div>
  <div class="service"><svg viewBox="0 0 48 48"><rect x="10" y="4" width="28" height="40" rx="2"/><path d="M16 14h16M16 22h16M16 30h10"/></svg>Business plan<br>development</div>
  <div class="service"><svg viewBox="0 0 48 48"><path d="M4 44h40M10 40V28M20 40V20M30 40V24M40 40V10M8 22l12-10 10 6 12-12"/></svg>Profit and growth<br>improvement</div>
  <div class="service"><svg viewBox="0 0 48 48"><rect x="4" y="8" width="40" height="28" rx="2"/><path d="M18 44h12M24 36v8M12 28l8-8 6 5 10-10"/></svg>Marketing consultancy<br>and advisory</div>
  <div class="service"><svg viewBox="0 0 48 48"><circle cx="10" cy="10" r="5"/><circle cx="38" cy="24" r="5"/><circle cx="10" cy="38" r="5"/><path d="M14 13l19 9M14 35l19-9"/></svg>Brand building<br>and strategy</div>
  <div class="service"><svg viewBox="0 0 48 48"><circle cx="24" cy="24" r="7"/><circle cx="24" cy="6" r="4"/><circle cx="24" cy="42" r="4"/><circle cx="6" cy="24" r="4"/><circle cx="42" cy="24" r="4"/><path d="M24 10v7M24 31v7M10 24h7M31 24h7"/></svg>Customer experience<br>mapping</div>
  <div class="service"><svg viewBox="0 0 48 48"><rect x="6" y="6" width="36" height="36" rx="2"/><path d="M6 16h36M14 26h20M14 34h12"/></svg>Digital footprint<br>optimisation</div>
  <div class="service"><svg viewBox="0 0 48 48"><path d="M6 20h10l18-10v28L16 28H6zM16 28l4 14h6"/></svg>Advertising</div>
</section>

<section class="funnel-section">
  <div class="funnel-title">MARKETING FUNNEL</div>
  <div class="funnel-art" role="img" aria-label="Illustrated marketing funnel with awareness, interest, decision and action stages"></div>
  <div class="funnel-copy">
    <h3>Focus on what matters the most</h3>
    <p>Grow your traffic and contribute more pipeline with a suite of services designed to deliver ideal prospects to sales.</p>
    <span class="btn">Learn more</span>
    <div class="dots"><span></span><span></span><span></span><span></span><span></span></div>
  </div>
</section>

<section class="cta-band">
  <div class="cta-panel">
    <h2>Ready to transform your business process and<br>marketing efforts?</h2>
    <p>Request a free assessment and get<br>started today</p>
    <span class="btn">Request a free 30 min consultation</span>
  </div>
</section>

<footer class="footer">
  <div class="contacts">
    <div class="contact"><div class="circle"><svg viewBox="0 0 28 28"><path d="M3 13l22-9-5 20-7-6-4 5v-7z"/></svg></div>Subscribe to our<br>newsletter</div>
    <div class="contact"><div class="circle"><svg viewBox="0 0 28 28"><path d="M7 3l4 5-2 3c1 3 4 6 7 7l3-2 5 4-2 4C12 24 4 16 4 6z"/></svg></div>Call now on<br>0400 555 019</div>
    <div class="contact"><div class="circle"><svg viewBox="0 0 28 28"><rect x="3" y="6" width="22" height="16" rx="2"/><path d="M3 7l11 8 11-8"/></svg></div>Contact us</div>
  </div>
  <div class="copyright">Copyright © 2020. Clearpath Advisory All Rights Reserved</div>
</footer>
</body>
</html>
```